Hops, Riffs & Sunset Grillout.

I need an A3 Poster, Insta Square and Facebook Event Cover photo for a Hops Riffs and Grill Event. Details as follows:

Name: Hops, Riffs and Sunset Grill
12pm - Late. Jan 26th at Copperleaf Yard Brewhouse
Acts:
Blue Tern - 7pm
Velvet Kite & Slow Morris - 3pm - 7pm
Grant Whitcombe - 12pm -3pm

Free BBQ 2-4pm.

```html
<!DOCTYPE html>
<html lang="en">
<head>
<meta charset="utf-8">
<title>Hops, Riffs &amp; Sunset Grillout – A3 Poster</title>
<link href="https://fonts.googleapis.com/css2?family=Alfa+Slab+One&family=Roboto+Slab:wght@400;600;700&display=swap" rel="stylesheet">
<style>
  :root {
    --page-bg: #9a9a9a;
    --poster-bg: #121314;
    --ink-white: #ffffff;
    --gold-top: #ffbe45;
    --gold-bottom: #ffdd33;
    --badge-red: #c81e0c;
    --wood: #6b4a2c;
    --wood-dark: #4a321c;
  }
  * { margin: 0; padding: 0; box-sizing: border-box; }
  html, body { width: 1200px; height: 1200px; overflow: hidden; }
  body { background: var(--page-bg); position: relative; font-family: "Roboto Slab", serif; }

  .poster {
    position: absolute; left: 201px; top: 35px; width: 798px; height: 1128px;
    background: var(--poster-bg); overflow: hidden; color: var(--ink-white);
  }
  .poster__photo {
    position: absolute; inset: 0;
    background:
      radial-gradient(ellipse 140px 300px at 384px 780px, rgba(230,150,30,0.9), rgba(180,100,20,0.5) 60%, transparent 100%),
      radial-gradient(ellipse 130px 110px at 640px 870px, rgba(150,55,20,0.8), transparent 100%),
      radial-gradient(ellipse 100px 80px at 60px 840px, rgba(140,90,40,0.6), transparent 100%),
      radial-gradient(ellipse 320px 260px at 560px 600px, rgba(40,55,70,0.7), transparent 100%),
      linear-gradient(180deg, #141414 0%, #191b1d 55%, #0d0d0d 100%);
  }

  .event-date {
    position: absolute; left: 322px; top: 68px;
    font-weight: 600; font-size: 24px; line-height: 30px; white-space: nowrap;
  }
  .event-title {
    position: absolute; left: 0; right: 0; top: 86px; text-align: center;
    font-family: "Alfa Slab One", serif; font-size: 200px; line-height: 1; letter-spacing: -3px;
    background: linear-gradient(90deg, var(--gold-top), var(--gold-bottom));
    -webkit-background-clip: text; background-clip: text; color: transparent;
  }
  .event-subtitle {
    position: absolute; left: 0; right: 0; top: 312px; text-align: center;
    font-family: "Alfa Slab One", serif; font-size: 40px; line-height: 1; font-weight: 400;
  }
  .time-sign {
    position: absolute; left: 286px; top: 374px; width: 226px; height: 50px;
    background: linear-gradient(180deg, var(--wood), var(--wood-dark));
    transform: rotate(-2deg);
    font-family: "Alfa Slab One", serif; font-size: 24px; line-height: 50px;
    text-align: center; color: #f2ece2; letter-spacing: 0.5px;
  }
  .bbq-badge {
    position: absolute; left: 49px; top: 751px; width: 214px; height: 214px;
    border-radius: 50%; background: var(--badge-red);
    display: flex; flex-direction: column; align-items: center; justify-content: center;
    font-family: "Alfa Slab One", serif; text-align: center;
  }
  .bbq-badge__main { font-size: 46px; line-height: 46px; }
  .bbq-badge__time { font-size: 28px; line-height: 34px; }

  .line-up {
    position: absolute; left: 45px; top: 980px;
    font-size: 22px; line-height: 27.5px; font-weight: 400;
  }
  .brand-mark {
    position: absolute; left: 618px; top: 1008px; width: 150px;
    font-family: "Roboto Slab", serif; font-weight: 700; font-size: 22px; line-height: 24px;
    text-align: center; text-transform: uppercase;
  }
</style>
</head>
<body>
  <main class="poster">
    <div class="poster__photo" role="img" aria-label="Photo of a splashing pint of golden beer with a burger, glazed chicken drumsticks and beer bottles on a dark table"></div>

    <h1 class="event-title">Hops</h1>
    <p class="event-date">Jan 26th at<br>Copperleaf Yard Brewhouse</p>
    <h2 class="event-subtitle">Riffs &amp; Sunset Grillout</h2>
    <div class="time-sign">12PM - LATE.</div>

    <div class="bbq-badge">
      <span class="bbq-badge__main">FREE</span>
      <span class="bbq-badge__main">BBQ</span>
      <span class="bbq-badge__time">2-4pm</span>
    </div>

    <p class="line-up">
      Acts:<br>
      Blue Tern - 7pm<br>
      Velvet Kite &amp; Slow Morris - 3pm - 7pm<br>
      Grant Whitcombe - 12pm -3pm
    </p>

    <div class="brand-mark">Copperleaf Yard Brewhouse</div>
  </main>
</body>
</html>
```